Commercial and Multifamily informational website

We need a website for our commercial real estate management company. We will manage offices, retail, apartments and others. Here is the brief verbiage: Providing quality commercial and multifamily portfolio management to Landlords, REITs, and financial institutions. 

Industry/Entity Type

Real Estate

Number of Pages Required

2 page

Font styles to use
Sans Serif
Other font styles liked:
• Muli, Garamond

Colors
0555a3
5c5c5c
3176b5
85acd3
474747

Requirements
Must have
• Home page and contact page

```html
<!DOCTYPE html>
<html lang="en">
<head>
<meta charset="utf-8">
<title>Kestrel Park Property Management – Contact</title>
<link href="https://fonts.googleapis.com/css2?family=Montserrat:wght@400;500;600&family=Mulish:wght@400;600;700&display=swap" rel="stylesheet">
<style>
:root{
  --blue:#0555a3;
  --blue-mid:#3176b5;
  --blue-light:#85acd3;
  --grey:#5c5c5c;
  --grey-dark:#474747;
  --page:#f3f5f8;
  --white:#ffffff;
  --line:#e3e6ea;
}
*{box-sizing:border-box;margin:0;padding:0}
html,body{width:876px;height:1200px;overflow:hidden}
body{background:var(--page);font-family:"Mulish",sans-serif;color:var(--grey);position:relative}

.hero{position:absolute;left:0;top:0;width:876px;height:420px;
  background:linear-gradient(180deg,#3d8fd8 0%,#9fc7ea 35%,#c9d3da 55%,#8d9a8a 72%,#4f7d3a 100%)}
.hero-cut{position:absolute;left:0;top:0}
.nav{position:absolute;left:214px;top:0;display:flex;height:68px}
.nav a{width:149px;display:flex;align-items:flex-end;justify-content:center;padding-bottom:15px;
  font-family:"Montserrat",sans-serif;font-weight:600;font-size:9.5px;color:var(--white);text-decoration:none;
  background:var(--blue);border-right:1px solid rgba(255,255,255,.15)}
.nav a:first-child{background:#1a6ec0;border-bottom-left-radius:4px}
.nav a.current{background:var(--blue-mid);width:148px}
.slide-arrow{position:absolute;top:229px;width:20px;height:20px;display:flex;align-items:center;justify-content:center}
.slide-arrow.prev{left:17px}
.slide-arrow.next{left:828px;background:var(--blue)}

.intro-box{position:absolute;left:212px;top:173px;width:449px;height:145px;background:rgba(255,255,255,.82);text-align:center;padding-top:28px}
.brand{font-family:"Montserrat",sans-serif;font-weight:600;color:var(--blue);font-size:21px;letter-spacing:.3px;display:inline-flex;align-items:center;gap:8px}
.brand-dot{width:10px;height:10px;background:var(--blue);display:inline-block}
.intro-box p{font-size:6.3px;line-height:10.5px;color:#222;width:290px;margin:24px auto 0}
.btn{display:inline-block;background:var(--blue);color:var(--white);font-family:"Montserrat",sans-serif;font-weight:600;font-size:6.5px;text-transform:uppercase;text-align:center}
.quote-btn{position:absolute;left:385px;top:347px;width:103px;height:24px;line-height:24px}
.home-badge{position:absolute;left:420px;top:394px;width:36px;height:36px;border-radius:50%;background:var(--white);display:flex;align-items:center;justify-content:center;box-shadow:0 1px 3px rgba(0,0,0,.15)}

.touch{position:absolute;top:454px;left:0;width:876px;text-align:center}
.touch h1{font-family:"Montserrat",sans-serif;font-weight:600;font-size:15px;color:var(--grey-dark);letter-spacing:.3px}
.touch p{font-size:6px;color:#9aa3ad;margin-top:9px}
.divider{position:absolute;top:499px;left:393px;width:90px;height:4px}

.card{position:absolute;top:527px;height:283px;background:var(--white);box-shadow:0 1px 4px rgba(0,0,0,.08)}
.info-card{left:171px;width:217px;padding:42px 0 0 41px}
.info-card h2{font-family:"Montserrat",sans-serif;font-weight:500;font-size:10.5px;color:var(--blue);margin-bottom:8px}
.info-card p{font-family:"Montserrat",sans-serif;font-size:7.5px;line-height:11px;color:#8a8f95;margin-bottom:25px}
.form-card{left:402px;width:303px;padding:42px 44px 0 45px}
.field{font-size:5.8px;font-weight:600;color:#8a8f95;border-bottom:1px solid var(--line);height:27px;padding-top:3px}
.field.message{height:47px}
.send-btn{margin-top:14px;width:72px;height:19px;line-height:19px}

.map{position:absolute;left:171px;top:823px;width:534px;height:119px;background:linear-gradient(90deg,#ece8df 0%,#e6e2d8 55%,#b8d1f0 75%,#e9e5dc 100%)}

.footer-band{position:absolute;left:0;top:949px;width:876px;height:211px;background:linear-gradient(90deg,#c7c9ce,#e5e6e9 40%,#e1e2e5 60%,#b9bbc1)}
.footer-brand{position:absolute;top:1006px;left:0;width:876px;text-align:center}
.footer-brand .brand{font-size:19px}
.office{position:absolute;left:0;width:876px;text-align:center;font-family:"Montserrat",sans-serif;font-weight:500;color:var(--blue);font-size:7.8px}
.office.label{top:1072px}
.office.line{top:1088px}
.to-top{position:absolute;left:826px;top:1146px;width:27px;height:27px;border-radius:50%;background:var(--blue);display:flex;align-items:center;justify-content:center;z-index:2}
.bottom-bar{position:absolute;left:0;top:1160px;width:876px;height:40px;background:#555558;display:flex;align-items:center;justify-content:space-between;padding:0 118px 0 171px}
.social{display:flex;gap:9px}
.social span{width:8px;height:8px;border-radius:50%;background:#a9abb0;display:block}
.copyright{font-size:5.5px;color:#d9dadd}
</style>
</head>
<body>

<header class="hero" role="img" aria-label="Photo of a suburban house with a garden under a blue sky"></header>
<svg class="hero-cut" width="876" height="430" viewBox="0 0 876 430" aria-hidden="true">
  <polygon points="0,364 438,418 876,364 876,430 0,430" fill="#f3f5f8"/>
</svg>

<nav class="nav">
  <a href="#">HOME</a>
  <a href="#">CONTACT US</a>
  <a href="#" class="current">SEARCH KESTREL PROPERTIES</a>
</nav>

<div class="slide-arrow prev"><svg width="8" height="10" viewBox="0 0 8 10"><path d="M6 1 2 5l4 4" fill="none" stroke="#ffffff" stroke-width="1.3"/></svg></div>
<div class="slide-arrow next"><svg width="8" height="10" viewBox="0 0 8 10"><path d="M2 1l4 4-4 4" fill="none" stroke="#ffffff" stroke-width="1.5"/></svg></div>

<section class="intro-box">
  <div class="brand"><span class="brand-dot"></span>Kestrel Park Property Management</div>
  <p>Lorem Ipsum is simply dummy text of the printing and typesetting industry. Lorem Ipsum has been the industry's standard dummy text ever since the 1500s, when an unknown printer took a galley of type and scrambled it to make a type specimen book.</p>
</section>
<a class="btn quote-btn">Get a quote</a>

<div class="home-badge">
  <svg width="16" height="14" viewBox="0 0 16 14"><path d="M8 0 0 7h2v7h4.5V9.5h3V14H14V7h2z" fill="#0555a3"/></svg>
</div>

<section class="touch">
  <h1>GET IN TOUCH</h1>
  <p>Nullam sit amet odio eu est aliquet euismod a a urna. Proin eu urna suscipit, dictum quam nec.</p>
</section>
<svg class="divider" viewBox="0 0 90 4" aria-hidden="true">
  <line x1="0" y1="2" x2="36" y2="2" stroke="#85acd3" stroke-width=".8"/>
  <circle cx="45" cy="2" r="1.8" fill="#0555a3"/>
  <line x1="54" y1="2" x2="90" y2="2" stroke="#85acd3" stroke-width=".8"/>
</svg>

<section class="card info-card">
  <h2>OUR ADDRESS</h2>
  <p>482 Alder Lane, Suite 210<br>3315 Brookfield, FL</p>
  <h2>CALL US</h2>
  <p>+ 555 014 220 7391<br>+ 0555018426</p>
  <h2>EMAIL US</h2>
  <p>hello@kestrelpark.com</p>
</section>

<section class="card form-card">
  <div class="field">Name*</div>
  <div class="field">Email*</div>
  <div class="field">Phone</div>
  <div class="field">Subject</div>
  <div class="field message">Message</div>
  <a class="btn send-btn">Send message</a>
</section>

<div class="map" role="img" aria-label="Street map showing the office location beside a river"></div>

<section class="footer-band" role="img" aria-label="Photo of hands passing house keys and a paper house cut-out"></section>
<div class="footer-brand"><div class="brand"><span class="brand-dot"></span>Kestrel Park Property Management</div></div>
<div class="office label">Office Address:</div>
<div class="office line">Lorem Ipsum is simply dummy text of the printing and typesetting</div>

<div class="to-top"><svg width="9" height="6" viewBox="0 0 9 6"><path d="M1 5l3.5-3.5L8 5" fill="none" stroke="#ffffff" stroke-width="1.3"/></svg></div>

<footer class="bottom-bar">
  <div class="social"><span></span><span></span><span></span><span></span></div>
  <div class="copyright">Kestrel Park Property Management © 2017 All Rights Reserved</div>
</footer>

</body>
</html>
```